Poster for Ballet Recital Tomasito y el Espejo Encantado

We need a poster for a ballet performance, we will be presenting "Tomasito y el Espejo Encantado".
We need something that looks magical, the word Tomasito as the main title in 3D gold texture and the text y el Espejo Encantado way smaller. We have included a reference of the Brelvo movie, just because we like the starry night background and the glowing moon. We don't want the two characters nor the flying carpet, because we will be adding a photo later.
The idea is for the poster to look magical, mysterious but fun. We want people to get the idea that the show will be very entertaining and worth their money.

Font styles to use
Decorative
Script

Colors

Designer to choose colors to be used in the design.

Requirements
Must have
• The title: Tomasito y el Espejo Encantado
• It must also include space for adding the ballet company logo, the dates, times and prices.
Nice to have
• Magical feel
Should not have
• Any photo or character illustration

```html
<!DOCTYPE html>
<html lang="es">
<head>
<meta charset="utf-8">
<title>Tomasito y el Espejo Encantado</title>
<link rel="stylesheet" href="https://fonts.googleapis.com/css2?family=Great+Vibes&family=Montserrat:wght@400&display=swap">
<style>
  :root {
    --night-deep: #02060f;
    --night-mid: #0a2350;
    --night-glow: #134a86;
    --moon-rim: #6fd6e8;
    --moon-core: rgba(40, 120, 170, 0.35);
    --gold-light: #fff4a3;
    --gold-mid: #e3b612;
    --gold-dark: #8a5a00;
    --ice: #86d9ea;
    --frame: #4f8fb8;
  }
  html, body {
    margin: 0;
    padding: 0;
    overflow: hidden;
    background: var(--night-deep);
  }
  .poster {
    position: relative;
    width: 848px;
    height: 1200px;
    overflow: hidden;
    background:
      radial-gradient(ellipse 420px 360px at 300px 300px, var(--night-glow), transparent 70%),
      radial-gradient(ellipse 380px 300px at 620px 650px, #0d3168, transparent 70%),
      radial-gradient(ellipse 500px 300px at 200px 1100px, #0b2a5a, transparent 70%),
      linear-gradient(180deg, var(--night-mid) 0%, #081a3c 55%, var(--night-deep) 100%);
    font-family: "Montserrat", sans-serif;
  }
  .frame {
    position: absolute;
    inset: 0;
  }
  .moon {
    position: absolute;
    left: 182px;
    top: 148px;
    width: 518px;
    height: 518px;
    border-radius: 50%;
    border: 2px solid var(--moon-rim);
    background: radial-gradient(circle at 50% 40%, var(--moon-core), rgba(10, 40, 90, 0.15) 70%, transparent);
    box-shadow: 0 0 40px rgba(111, 214, 232, 0.35), inset 0 0 60px rgba(111, 214, 232, 0.2);
  }
  .moon::before {
    content: "";
    position: absolute;
    left: 50%;
    top: -10px;
    width: 120px;
    height: 30px;
    transform: translateX(-50%);
    background: radial-gradient(ellipse, rgba(160, 240, 255, 0.8), transparent 70%);
  }
  .title {
    position: absolute;
    left: 0;
    right: 0;
    margin: 0;
    text-align: center;
    font-family: "Great Vibes", cursive;
    font-weight: 400;
    background: linear-gradient(180deg, var(--gold-light) 0%, var(--gold-mid) 45%, var(--gold-dark) 60%, var(--gold-mid) 80%, var(--gold-light) 100%);
    -webkit-background-clip: text;
    background-clip: text;
    color: transparent;
    filter: drop-shadow(2px 3px 2px rgba(0, 0, 0, 0.6));
  }
  .title-main {
    top: 210px;
    font-size: 168px;
    line-height: 1;
  }
  .title-sub {
    top: 468px;
    font-size: 52px;
    line-height: 1;
  }
  .dancers {
    position: absolute;
    left: 356px;
    top: 572px;
    width: 158px;
    height: 208px;
  }
  .schedule {
    position: absolute;
    left: 60px;
    top: 855px;
    width: 728px;
    display: grid;
    grid-template-columns: 1fr 1fr 1fr;
    text-align: center;
  }
  .schedule-heading {
    margin: 0 0 42px;
    font-family: "Great Vibes", cursive;
    font-weight: 400;
    font-size: 46px;
    line-height: 1;
    background: linear-gradient(180deg, var(--gold-light), var(--gold-mid) 50%, var(--gold-dark));
    -webkit-background-clip: text;
    background-clip: text;
    color: transparent;
  }
  .schedule-list {
    list-style: none;
    margin: 0;
    padding: 0;
    color: var(--ice);
    font-size: 22px;
    line-height: 35px;
    letter-spacing: 0.5px;
  }
</style>
</head>
<body>
<main class="poster">
  <svg class="frame" width="848" height="1200" viewBox="0 0 848 1200" aria-hidden="true">
    <g stroke="var(--frame)" stroke-width="1.5" fill="none">
      <line x1="62" y1="51" x2="786" y2="51"/>
      <line x1="62" y1="1141" x2="786" y2="1141"/>
      <line x1="51" y1="60" x2="51" y2="254"/>
      <line x1="797" y1="60" x2="797" y2="254"/>
      <line x1="51" y1="746" x2="51" y2="1136"/>
      <line x1="797" y1="746" x2="797" y2="1136"/>
    </g>
    <g stroke="#cfe7f2" stroke-width="1.5">
      <line x1="288" y1="933" x2="288" y2="1102"/>
      <line x1="579" y1="933" x2="579" y2="1102"/>
    </g>
  </svg>

  <div class="moon"></div>

  <h1 class="title title-main">Tomasito</h1>
  <p class="title title-sub">y el Espejo Encantado</p>

  <svg class="dancers" viewBox="0 0 158 208" role="img" aria-label="Silhouette of two ballet dancers in a lift">
    <rect width="158" height="208" rx="20" fill="#7fd3ea" opacity="0.85"/>
  </svg>

  <section class="schedule">
    <div class="schedule-col">
      <h2 class="schedule-heading">dates</h2>
      <ul class="schedule-list">
        <li>23.06.2019.</li>
        <li>23.06.2019.</li>
        <li>23.06.2019.</li>
        <li>23.06.2019.</li>
      </ul>
    </div>
    <div class="schedule-col">
      <h2 class="schedule-heading">times</h2>
      <ul class="schedule-list">
        <li>04 pm</li>
        <li>06 pm</li>
        <li>08 pm</li>
        <li>10 pm</li>
      </ul>
    </div>
    <div class="schedule-col">
      <h2 class="schedule-heading">prices</h2>
      <ul class="schedule-list">
        <li>&amp; 14</li>
        <li>&amp; 16</li>
        <li>&amp; 18</li>
        <li>&amp; 20</li>
      </ul>
    </div>
  </section>
</main>
</body>
</html>
```